Kestrel Bay Warehousing Group Needs A Website

We are looking for a website for a new company. 4 Pages

Needs to be responsive and mobile friendly for all browsers and coded for both Android & IOS. SEO is also important.

Website Brief – Kestrel Bay Warehousing Group
Domain: www.kestrelbaywarehousing.com
Email: info@kestrelbaywarehousing.com
Phone: to be inserted later
Address: 10458 82 Ave, Edmonton, AB T6E 2K9
Platform: WordPress (recommended for flexibility, SEO tools, and ease of editing)
Requirements:
• Responsive & mobile-friendly (Android & iOS)
• Cross-browser compatibility
• Fast page load speed
• SEO optimized for storage development, management, and investment keywords
• Easy in-house editing after launch
• Professional, modern, trust-driven design reflecting expertise, reliability, and innovation
________________________________________
Pages
1. HOME
Purpose: Quickly communicate who Kestrel Bay Warehousing Group is and why they’re the best choice for designing, building, leasing, and managing self storage facilities.
Content Highlights:
• Hero Section: Large, bold image of a modern self storage facility with headline:
"From Concept to Capacity – Your Self Storage Experts"
• Subheadline: “Kestrel Bay Warehousing Group delivers turnkey design, construction, leasing, and management services for profitable self storage operations.”
• Quick Service Icons:
o Facility Design & Development
o Construction & Build Management
o Lease-Up & Marketing
o Ongoing Facility Management
• Call to Action Button: “LEARN MORE” → links to ABOUT US page.
• Featured Project Highlights: Showcase a few completed or current projects with photos and stats.
• Contact Banner: “Ready to build your next self storage project? Let’s talk.” → CONTACT page.
2. ABOUT US
Purpose: Build credibility, showcase experience, and explain the value proposition.
Content Highlights:
• Who We Are: Overview of Kestrel Bay Warehousing Group’ history, mission, and team expertise.
• Our Approach: End-to-end process from site selection to occupancy.
• Why Choose Us:
o Industry expertise in self storage
o Proven track record in lease-up success
o Strong vendor and contractor network
3. SERVICES
Purpose: Detail all service offerings with clarity and authority.
Sections:
• Design & Development: Market analysis, site planning, and architectural design.
• Construction Management: Overseeing timelines, budgets, and quality control.
• Lease-Up Strategy: Marketing, promotions, and occupancy acceleration.
• Ongoing Facility Management: Staffing, maintenance, revenue optimization.

4. CONTACT
Purpose: Provide simple, direct ways to connect.
Content Highlights:
• Contact Form (Name, Email, Phone, Message)
• Direct Email: info@kestrelbaywarehousing.com
• Phone (if applicable)
• Google Map embed (if there’s a head office location)
• CTA: “Let’s Build Your Storage Success Story.”
Design & Technical Notes
• Visual Style: Clean, modern, bold typography, professional color palette (to be based on branding), strong imagery of self storage facilities.
• Performance: Image compression, caching, responsive scaling.
• SEO Targets: “Self storage facility developer,” “self storage construction,” “self storage management company,” “lease-up services for self storage.”

WordPress or Joomla – must be desktop and mobile friendly with fast page load speed. Need the ability to edit ourselves.

Use pantone colours - #033c5a – dark blue
#2baadf – light blue

```html
<!DOCTYPE html>
<html lang="en">
<head>
<meta charset="utf-8">
<title>Kestrel Bay Warehousing Group – Self Storage Experts</title>
<link href="https://fonts.googleapis.com/css2?family=Lexend:wght@300;400;500;600;700&display=swap" rel="stylesheet">
<style>
:root{
  --navy:#033c5a;
  --navy-deep:#0d2a4d;
  --blue:#2baadf;
  --ink:#1c2a3a;
  --muted:#5e6b78;
  --band:#dff0fa;
  --line:#d6dbe0;
  --white:#ffffff;
}
*{margin:0;padding:0;box-sizing:border-box}
html,body{width:1200px;height:2702px;overflow:hidden}
body{font-family:"Lexend",sans-serif;color:var(--ink);background:var(--white);position:relative}
.abs{position:absolute}
a{color:inherit;text-decoration:none}

/* header */
.site-header{position:absolute;left:0;top:0;width:1200px;height:68px;background:var(--white);z-index:5}
.brand{position:absolute;left:155px;top:22px;display:flex;align-items:center;gap:9px;font-weight:700;font-size:16px;color:var(--navy)}
.brand .mark{width:24px;height:24px;background:var(--navy)}
.main-nav a{position:absolute;top:25px;font-size:13px;color:var(--ink)}
.main-nav a.active{color:var(--blue);text-decoration:underline;text-underline-offset:4px}
.icon-btn{position:absolute;top:20px;width:30px;height:30px;border-radius:50%;background:var(--navy);display:flex;align-items:center;justify-content:center}
.btn{display:flex;align-items:center;justify-content:center;background:var(--navy);color:var(--white);font-weight:600;font-size:12px;border-radius:2px;position:absolute}

/* hero */
.hero-art{position:absolute;left:0;top:0}
.hero-title{position:absolute;left:0;width:1200px;top:236px;text-align:center;color:var(--white);font-weight:700;font-size:44px;line-height:51px}
.hero-sub{position:absolute;left:0;width:1200px;top:346px;text-align:center;color:var(--white);font-weight:500;font-size:13px;line-height:19px}

.section-title{position:absolute;left:0;width:1200px;text-align:center;font-weight:700;font-size:30px;color:var(--navy)}

/* services */
.service-card{position:absolute;top:769px;width:208px;height:224px;background:var(--white);box-shadow:0 2px 14px rgba(3,60,90,.08)}
.service-card svg{position:absolute;left:18px;top:40px}
.service-card h3{position:absolute;left:18px;top:119px;font-size:15px;line-height:16px;font-weight:700;color:var(--navy)}
.service-card p{position:absolute;left:18px;top:162px;width:180px;font-size:11.5px;line-height:17px;color:var(--muted);font-weight:300}

/* projects */
.projects-band{position:absolute;left:0;top:1131px;width:1200px;height:734px;background:var(--band);overflow:hidden}
.shot{position:absolute;border-radius:3px}
.caption{position:absolute;top:430px;width:437px;height:130px;overflow:hidden;background:var(--white);border-radius:4px;box-shadow:0 4px 18px rgba(3,60,90,.12);padding:14px 18px}
.caption h4{font-size:14.5px;line-height:18px;color:var(--blue);font-weight:700;white-space:nowrap}
.tags{display:flex;gap:8px;margin-top:9px}
.tags span{border:1px solid var(--line);font-size:10px;line-height:14px;padding:1px 9px;color:var(--navy);white-space:nowrap}
.caption p{margin-top:9px;font-size:10px;line-height:15px;color:var(--ink);font-weight:300;white-space:nowrap;padding-right:30px}
.go{position:absolute;right:16px;top:88px;width:18px;height:18px;border-radius:50%;background:var(--blue);display:flex;align-items:center;justify-content:center}
.faded{opacity:.45}
.dots{position:absolute;top:1717px;left:546px;display:flex;gap:12px}
.dots i{width:11px;height:11px;border:1.5px solid var(--blue);border-radius:50%;display:block}
.dots i.on{background:radial-gradient(var(--blue) 45%,transparent 50%)}

/* form */
.field{position:absolute;border:1px solid var(--line);font-size:11px;color:#8a949e;padding:0 12px;display:flex;align-items:center;font-weight:300}
.field.area{align-items:flex-start;padding-top:10px}

/* footer */
.footer-art{position:absolute;left:0;top:2290px}
.cta-text{position:absolute;left:347px;top:2412px;font-size:17.5px;font-weight:700;color:var(--white)}
.divider{position:absolute;left:200px;top:2473px;width:800px;height:1px;background:rgba(255,255,255,.12)}
.foot-brand{position:absolute;left:155px;top:2554px;display:flex;align-items:center;gap:10px;font-size:19px;font-weight:700;color:var(--white)}
.foot-brand .mark{width:32px;height:32px;background:var(--blue)}
.foot-col h5{position:absolute;top:2512px;font-size:14px;font-weight:600;color:var(--blue)}
.foot-item{position:absolute;font-size:12px;color:var(--white);display:flex;gap:9px;line-height:16px;font-weight:300}
.foot-link{position:absolute;font-size:12.5px;color:var(--white);font-weight:300}
.bottom-bar{position:absolute;left:0;top:2668px;width:1200px;height:34px;background:var(--blue)}
.bottom-bar p{position:absolute;left:155px;top:10px;font-size:11px;color:var(--white);font-weight:300}
.social{position:absolute;top:9px;width:15px;height:15px;background:var(--navy-deep);border-radius:2px}
</style>
</head>
<body>

<svg class="hero-art" width="1200" height="640" viewBox="0 0 1200 640">
  <defs>
    <linearGradient id="heroFill" x1="0" y1="0" x2="1" y2="1">
      <stop offset="0" stop-color="#3d5c86"/>
      <stop offset=".5" stop-color="#2b4c78"/>
      <stop offset="1" stop-color="#1c3d66"/>
    </linearGradient>
  </defs>
  <path d="M0 68H1200V420Q1200 462 1160 476L650 622Q600 638 550 622L40 476Q0 462 0 420Z" fill="var(--navy-deep)"/>
  <path d="M250 520L560 610Q600 622 640 610L950 520L650 600Q600 614 550 600Z" fill="var(--blue)"/>
  <path d="M0 68H1200V420Q1200 462 1160 476L650 596Q600 608 550 596L40 476Q0 462 0 420Z" fill="url(#heroFill)" role="img" aria-label="Photo of a business team with hands together over a laptop, overlaid with a dark blue tint"/>
</svg>

<header class="site-header">
  <a class="brand" href="#"><span class="mark"></span>Kestrel Bay Warehousing Group</a>
  <nav class="main-nav">
    <a class="active" href="#" style="left:485px">Home</a>
    <a href="#" style="left:549px">About Us</a>
    <a href="#" style="left:632px">Services</a>
    <a href="#" style="left:710px">Contact Us</a>
  </nav>
  <a class="icon-btn" href="#" style="left:813px" aria-label="Call">
    <svg width="13" height="13" viewBox="0 0 24 24"><path d="M6.6 10.8a15 15 0 006.6 6.6l2.2-2.2a1 1 0 011-.25 11.4 11.4 0 003.6.6 1 1 0 011 1V20a1 1 0 01-1 1A17 17 0 013 4a1 1 0 011-1h3.5a1 1 0 011 1 11.4 11.4 0 00.6 3.6 1 1 0 01-.25 1z" fill="#fff"/></svg>
  </a>
  <a class="icon-btn" href="#" style="left:849px" aria-label="Email">
    <svg width="13" height="13" viewBox="0 0 24 24"><rect x="3" y="5" width="18" height="14" rx="2" fill="#fff"/><path d="M3 7l9 6 9-6" stroke="#033c5a" stroke-width="2" fill="none"/></svg>
  </a>
  <a class="btn" href="#" style="left:898px;top:19px;width:146px;height:31px">Get a Free Estimate</a>
</header>

<h1 class="hero-title">From Concept To Capacity<br>Your Self Storage Experts</h1>
<p class="hero-sub">Kestrel Bay Warehousing Group Delivers Turnkey Design, Construction, Leasing, And Management<br>Services For Profitable Self Storage Operations.</p>

<h2 class="section-title" style="top:707px">Our Services</h2>

<article class="service-card" style="left:156px">
  <svg width="52" height="52" viewBox="0 0 52 52"><circle cx="26" cy="26" r="22" fill="none" stroke="var(--navy)" stroke-width="2.5" stroke-dasharray="8 3"/><circle cx="26" cy="26" r="14" fill="var(--blue)"/><path d="M26 16l5 10-5 8-5-8z" fill="none" stroke="var(--navy)" stroke-width="2"/></svg>
  <h3>Design &amp;<br>Development</h3>
  <p>Market analysis, site planning, and architectural design.</p>
</article>
<article class="service-card" style="left:383px">
  <svg width="52" height="52" viewBox="0 0 52 52"><path d="M6 30a20 20 0 0140 0z" fill="var(--blue)" stroke="var(--navy)" stroke-width="2.5"/><rect x="4" y="30" width="44" height="5" fill="var(--navy)"/><path d="M14 36a12 12 0 0024 0" fill="none" stroke="var(--navy)" stroke-width="2.5"/><path d="M26 10v10" stroke="var(--navy)" stroke-width="2.5"/></svg>
  <h3>Construction<br>Management</h3>
  <p>Overseeing timelines, budgets, and quality control.</p>
</article>
<article class="service-card" style="left:609px">
  <svg width="52" height="52" viewBox="0 0 52 52"><circle cx="26" cy="26" r="22" fill="none" stroke="var(--navy)" stroke-width="2.5"/><path d="M8 20a20 20 0 0118-14" fill="none" stroke="var(--blue)" stroke-width="4"/><circle cx="17" cy="30" r="3" fill="none" stroke="var(--navy)" stroke-width="2"/><path d="M20 28l10-8M31 30l4 4M35 30l-4 4" stroke="var(--navy)" stroke-width="2"/></svg>
  <h3>Lease-Up<br>Strategy</h3>
  <p>Marketing, promotions, and occupancy acceleration.</p>
</article>
<article class="service-card" style="left:836px">
  <svg width="52" height="52" viewBox="0 0 52 52"><circle cx="26" cy="12" r="6" fill="none" stroke="var(--navy)" stroke-width="2.5"/><circle cx="16" cy="18" r="5" fill="none" stroke="var(--navy)" stroke-width="2.5"/><circle cx="36" cy="18" r="5" fill="none" stroke="var(--navy)" stroke-width="2.5"/><path d="M10 30a16 16 0 0032 0" fill="var(--blue)" stroke="var(--navy)" stroke-width="2.5"/><rect x="8" y="26" width="36" height="4" fill="var(--navy)"/></svg>
  <h3>Ongoing Facility<br>Management</h3>
  <p>Staffing, maintenance, revenue optimization.</p>
</article>

<a class="btn" href="#" style="left:554px;top:1025px;width:100px;height:31px">Learn More</a>

<section class="projects-band">
  <h2 class="section-title" style="top:72px">Current Projects</h2>

  <div class="shot faded" style="left:-10px;top:133px;width:272px;height:387px;background:linear-gradient(135deg,#c9d4e0,#6d85a3 55%,#3d4f66)" role="img" aria-label="Website screenshot of a business consulting homepage with people working at a laptop"></div>
  <div class="caption faded" style="left:-269px">
    <h4>Developed Lorem Ipsum Is Simply Dummy Text<br>Of The Printing And Typesetting Industry.</h4>
    <div class="tags"><span>Web Development</span><span>Website Design</span></div>
    <p>Lorem Ipsum Is Simply Dummy Text Of The Printing And Typesetting Industry.<br>Lorem Ipsum Has Been The Industry's Standard...</p>
    <span class="go"><svg width="10" height="10" viewBox="0 0 10 10"><path d="M2 5h6M5.5 2.5L8 5 5.5 7.5" stroke="#fff" stroke-width="1.4" fill="none"/></svg></span>
  </div>

  <div class="shot" style="left:287px;top:133px;width:563px;height:387px;background:linear-gradient(120deg,#2a2622,#6b6258 55%,#b8b2aa 80%,#8a2a2a)" role="img" aria-label="Website screenshot of a real estate homepage with a model house and a call today banner"></div>
  <div class="caption" style="left:319px">
    <h4>Developed Lorem Ipsum Is Simply Dummy Text<br>Of The Printing And Typesetting Industry.</h4>
    <div class="tags"><span>Web Development</span><span>Website Design</span></div>
    <p>Lorem Ipsum Is Simply Dummy Text Of The Printing And Typesetting Industry.<br>Lorem Ipsum Has Been The Industry's Standard...</p>
    <span class="go"><svg width="10" height="10" viewBox="0 0 10 10"><path d="M2 5h6M5.5 2.5L8 5 5.5 7.5" stroke="#fff" stroke-width="1.4" fill="none"/></svg></span>
  </div>

  <div class="shot" style="left:875px;top:133px;width:340px;height:387px;background:linear-gradient(160deg,#163a4e,#2c5468 50%,#7a4a30)" role="img" aria-label="Website screenshot of a logistics company homepage with shipping containers"></div>
  <div class="caption" style="left:906px">
    <h4>Developed Lorem Ipsum Is Simply Dummy Text<br>Of The Printing And Typesetting Industry.</h4>
    <div class="tags"><span>Web Development</span><span>Website Design</span></div>
    <p>Lorem Ipsum Is Simply Dummy Text Of The Printing And Typesetting Industry.<br>Lorem Ipsum Has Been The Industry's Standard...</p>
  </div>
  <div class="abs" style="left:1060px;top:0;width:140px;height:734px;background:linear-gradient(90deg,rgba(223,240,250,0),rgba(223,240,250,.9))"></div>
</section>
<div class="dots"><i></i><i></i><i class="on"></i><i></i><i></i></div>
<a class="btn" href="#" style="left:559px;top:1760px;width:81px;height:31px">View All</a>

<h2 class="section-title" style="top:1930px">Quick Inquiry</h2>
<div class="field" style="left:325px;top:1991px;width:268px;height:34px">First Name</div>
<div class="field" style="left:606px;top:1991px;width:268px;height:34px">Last Name</div>
<div class="field" style="left:325px;top:2040px;width:268px;height:34px">Email</div>
<div class="field" style="left:606px;top:2040px;width:268px;height:34px">Phone</div>
<div class="field area" style="left:325px;top:2090px;width:549px;height:79px">How Can We Help?</div>
<a class="btn" href="#" style="left:562px;top:2201px;width:76px;height:31px">Submit</a>

<svg class="footer-art" width="1200" height="380" viewBox="0 2290 1200 380">
  <path d="M180 2405L560 2300Q600 2290 640 2300L1020 2405L640 2312Q600 2302 560 2312Z" fill="var(--blue)"/>
  <path d="M0 2668V2492Q0 2452 40 2442L556 2322Q600 2312 644 2322L1160 2442Q1200 2452 1200 2492V2668Z" fill="var(--navy-deep)"/>
</svg>
<p class="cta-text">Ready to build your next self storage project?</p>
<a class="btn" href="#" style="left:764px;top:2413px;width:87px;height:27px;background:var(--navy);font-size:11.5px">Let’s talk</a>
<div class="divider"></div>

<div class="foot-brand"><span class="mark"></span>Kestrel Bay<br>Warehousing Group</div>

<div class="foot-col">
  <h5 style="left:421px">Contact Us</h5>
  <div class="foot-item" style="left:421px;top:2543px">
    <svg width="11" height="11" viewBox="0 0 24 24"><path d="M6.6 10.8a15 15 0 006.6 6.6l2.2-2.2a1 1 0 011-.25 11.4 11.4 0 003.6.6 1 1 0 011 1V20a1 1 0 01-1 1A17 17 0 013 4a1 1 0 011-1h3.5a1 1 0 011 1 11.4 11.4 0 00.6 3.6 1 1 0 01-.25 1z" fill="var(--blue)"/></svg>(780) 555-0147</div>
  <div class="foot-item" style="left:421px;top:2569px">
    <svg width="11" height="11" viewBox="0 0 24 24"><rect x="3" y="5" width="18" height="14" rx="2" fill="var(--blue)"/><path d="M3 7l9 6 9-6" stroke="#0d2a4d" stroke-width="2" fill="none"/></svg>info@kestrelbaywarehousing.com</div>
  <div class="foot-item" style="left:421px;top:2596px">
    <svg width="11" height="14" viewBox="0 0 24 30"><path d="M12 0a10 10 0 0110 10c0 8-10 20-10 20S2 18 2 10A10 10 0 0112 0z" fill="var(--blue)"/><circle cx="12" cy="10" r="4" fill="#0d2a4d"/></svg>10458 82 Ave, Edmonton,<br>AB T6E 2K9</div>

  <h5 style="left:647px">Quick Inquiry</h5>
  <a class="foot-link" href="#" style="left:649px;top:2544px;color:var(--blue);text-decoration:underline">Home</a>
  <a class="foot-link" href="#" style="left:649px;top:2568px">About Us</a>
  <a class="foot-link" href="#" style="left:649px;top:2591px">Services</a>
  <a class="foot-link" href="#" style="left:649px;top:2615px">Contact Us</a>
</div>

<div class="abs" style="left:794px;top:2513px;width:250px;height:115px;border-radius:4px;background:linear-gradient(135deg,#eef1f4,#dde3ea)" role="img" aria-label="Map of the head office location in Edmonton"></div>

<footer class="bottom-bar">
  <p>© 2025 Kestrel Bay Warehousing Group. All Rights Reserved.</p>
  <span class="social" style="left:964px"></span>
  <span class="social" style="left:993px"></span>
  <span class="social" style="left:1020px;top:6px;width:22px;height:22px;border-radius:50%"></span>
</footer>

</body>
</html>
```